Poetry Book Cover Design Project

Looking for a minimalistic book cover design for a collection of poems. The book title is "Before The Morning Turns To Glass". There are three parts to the book. First covers poetry in the theme of Rage. Second love and desire. The third is strange poems. Essentially the sections are "Rage", "Desire" and the "Strange". The reason for the title "Before The Morning Turns To Glass" is as if someone is writing these till life changes towards the intended outcome as felt in each poem. I want to have the author's name "Nirosha Kulathunge" at the bottom. Ilustration attached.
- Minimalistic

```html
<!DOCTYPE html>
<html lang="en">
<head>
<meta charset="utf-8">
<title>Before The Morning Turns To Glass — Cover</title>
<link rel="stylesheet" href="https://fonts.googleapis.com/css2?family=Bodoni+Moda:opsz,wght@6..96,400;6..96,500&family=Josefin+Sans:wght@400&display=swap">
<style>
  :root {
    --backdrop: #d9cfc7;
    --cover: #050505;
    --ink: #f4f4f4;
    --ink-soft: #e6e6e6;
  }
  * { margin: 0; padding: 0; box-sizing: border-box; }
  html, body {
    width: 1200px;
    height: 800px;
    overflow: hidden;
    background: var(--backdrop);
  }
  .stage {
    width: 1200px;
    height: 800px;
    display: flex;
    align-items: center;
    justify-content: center;
  }
  .book-cover {
    position: relative;
    width: 500px;
    height: 720px;
    background: var(--cover);
    color: var(--ink);
    box-shadow: 0 10px 30px rgba(0,0,0,0.18);
  }
  .title {
    position: absolute;
    top: 70px;
    left: 0;
    right: 0;
    display: flex;
    flex-direction: column;
    align-items: center;
    font-family: "Bodoni Moda", "Didot", serif;
    font-weight: 400;
    text-transform: uppercase;
    line-height: 1.02;
  }
  .title__line {
    display: block;
    transform: scale(0.74, 1.18);
    transform-origin: center;
    white-space: nowrap;
  }
  .title__line--large { font-size: 100px; letter-spacing: -2px; }
  .title__line--medium { font-size: 70px; letter-spacing: -1px; }
  .title__line--small { font-size: 54px; letter-spacing: 0; }
  .title__cap { font-size: 1.18em; }
  .author {
    position: absolute;
    left: 58px;
    bottom: 62px;
    font-family: "Josefin Sans", "Helvetica Neue", sans-serif;
    font-size: 17px;
    letter-spacing: 8px;
    line-height: 2.1;
    text-transform: uppercase;
    color: var(--ink-soft);
  }
  .author__line { display: block; }
</style>
</head>
<body>
  <main class="stage">
    <section class="book-cover" aria-label="Book cover">
      <h1 class="title">
        <span class="title__line title__line--large">Before</span>
        <span class="title__line title__line--medium">The</span>
        <span class="title__line title__line--large">Morning</span>
        <span class="title__line title__line--small">Turns To</span>
        <span class="title__line title__line--large"><span class="title__cap">G</span>lass</span>
      </h1>
      <p class="author">
        <span class="author__line">Nirosha</span>
        <span class="author__line">Kulathunge</span>
      </p>
    </section>
  </main>
</body>
</html>
```